Win a Trip To Japan Poster

Our business offers ski holidays to Japan.

During July and August we will be giving away weekly pruct from Brenvik, then at the end of the winter we will give away a trip for 2 to Japan including all flights, 7 nights accommodation, lift passes, transport, breakfasts and in resort hosting. Flights are from any Australian calital city flying Coralwind Airways, then accommodation is at The Nook Tervale (we own this property) www.thenooktervale.example, the trip is valued over $6000.

We must include our logo, Brenvik (as we are giving away there product) and Coralwind Airways as they have donated the flights.

To enter this competition people will have to 'like' us on facebook, the facebook address is: www.friendloop.example/frostpinetravel from our Friendloop fans we will be giving away and announcing all prizes.

our company website is www.powder-lodges-north.example and we will be putting these posters up in Australian and NZ snow fields. We will require the poster to be A3 in size and also an A4 (flyer version) and in a Jpeg format we can use as the welcome page to our facebook site. Following this there will be a number of on going design projects.

Target Market(s)

22-35 year old skiiers and snowboarders

Industry/Entity Type

Accommodation

Requirements
Must have
• Our logo, Coralwind Airways Logo, Brenvik Logo

```html
<!DOCTYPE html>
<html lang="en">
<head>
<meta charset="utf-8">
<title>Win a Trip to Japan</title>
<link href="https://fonts.googleapis.com/css2?family=Limelight&family=Archivo+Black&display=swap" rel="stylesheet">
<style>
  :root {
    --red: #d9251d;
    --white: #ffffff;
    --grey-band: #dcdcdc;
    --muted: #d9d0cc;
    --ink: #111111;
    --airline: #3a3a6a;
    --social: #3b5a9a;
    --scene-dark: #4a4548;
    --scene-mid: #9a9a9e;
    --scene-light: #e4e4e6;
    --deco: 'Limelight', 'Times New Roman', serif;
    --block: 'Archivo Black', Arial, sans-serif;
  }
  * { margin: 0; padding: 0; box-sizing: border-box; }
  html, body { width: 1200px; height: 867px; overflow: hidden; background: var(--white); }
  .poster { position: relative; width: 1200px; height: 867px; background: var(--white); overflow: hidden; }

  .side-panel { position: absolute; left: 0; top: 0; width: 387px; height: 867px; background: var(--red); }
  .headline { position: absolute; left: 66px; top: 34px; font-family: var(--deco); font-weight: normal;
    color: var(--white); font-size: 76px; line-height: 84px; letter-spacing: 1px; white-space: nowrap; }
  .entry-copy { position: absolute; left: 68px; top: 432px; font-family: var(--deco); color: var(--muted);
    font-size: 17px; line-height: 21.5px; letter-spacing: 0.3px; text-transform: uppercase; white-space: nowrap; }
  .entry-copy .initial { font-size: 30px; }
  .fan-link { position: absolute; left: 68px; top: 628px; font-family: var(--deco); color: var(--muted);
    font-size: 16px; line-height: 22px; text-decoration: underline; white-space: nowrap; }
  .info-note { position: absolute; left: 68px; top: 718px; font-family: var(--deco); color: var(--muted);
    font-size: 10px; line-height: 14px; text-transform: uppercase; white-space: nowrap; }
  .info-note span { text-decoration: underline; text-transform: none; }
  .client-name { position: absolute; left: 4px; top: 804px; font-family: var(--block); color: var(--ink);
    font-size: 13px; letter-spacing: -0.2px; white-space: nowrap; }
  .sponsor-name { position: absolute; left: 218px; top: 808px; font-family: var(--block); color: var(--ink);
    font-size: 18px; letter-spacing: 3px; white-space: nowrap; }

  .grey-band { position: absolute; left: 445px; top: 88px; width: 755px; height: 264px; background: var(--grey-band); }
  .win-get { position: absolute; left: 585px; top: 94px; font-family: var(--deco); color: var(--red);
    font-size: 36px; letter-spacing: 1px; white-space: nowrap; }
  .prize-box { position: absolute; left: 792px; top: 0; width: 371px; height: 447px; background: var(--red);
    font-family: var(--deco); color: var(--white); }
  .prize-box h2 { position: absolute; left: 26px; top: 90px; font-size: 18px; font-weight: normal;
    letter-spacing: 1px; white-space: nowrap; }
  .prize-box ul { position: absolute; left: 70px; top: 138px; font-size: 18px; line-height: 21px;
    letter-spacing: 0.5px; list-style: disc; white-space: nowrap; }
  .prize-box .value { position: absolute; left: 56px; top: 284px; font-size: 17px; letter-spacing: 0.5px; white-space: nowrap; }
  .awaits { position: absolute; left: 397px; top: 360px; font-family: var(--deco); color: var(--red);
    font-size: 30px; letter-spacing: 1px; white-space: nowrap; }

  .resort-scene { position: absolute; left: 395px; top: 447px; width: 770px; height: 355px;
    background: linear-gradient(180deg, var(--scene-mid) 0%, var(--scene-dark) 45%, var(--scene-mid) 70%, var(--scene-light) 100%); }

  .airline-name { position: absolute; left: 393px; top: 810px; font-family: var(--block); color: var(--airline);
    font-size: 13px; letter-spacing: 0.5px; white-space: nowrap; }
  .social-mark { position: absolute; left: 614px; top: 790px; }
  .fine-print { position: absolute; left: 705px; top: 798px; font-family: var(--block); color: var(--ink);
    font-size: 12px; line-height: 16px; white-space: nowrap; }
</style>
</head>
<body>
<main class="poster">
  <section class="side-panel">
    <h1 class="headline">WIN A<br>TRIP<br>TO<br>JAPAN</h1>
    <p class="entry-copy"><span class="initial">T</span>o enter this<br>competition ‘like’ us on<br>Friendloop today<br>following the link<br>given below. All prizes<br>will be announced<br>from our Friendloop<br>fans.</p>
    <p class="fan-link">www.friendloop.example/<br>frostpinetravel</p>
    <p class="info-note">For further information log onto<br><span>www.powder-lodges-north.example</span></p>
    <p class="client-name">FROSTPINE SNOW TOURS</p>
    <p class="sponsor-name">BRENVIK</p>
  </section>

  <div class="grey-band"></div>
  <p class="win-get">WIN N GET</p>

  <section class="prize-box">
    <h2>A TRIP FOR TWO INCLUDING:</h2>
    <ul>
      <li>ALL FLIGHTS</li>
      <li>7 NIGHT ACCOMMODATION</li>
      <li>LIFT PASSES</li>
      <li>TRANSPORT</li>
      <li>BREAKFASTS</li>
      <li>IN RESORT HOSTING</li>
    </ul>
    <p class="value">—valued at over $6000.</p>
  </section>

  <p class="awaits">NOOK TERVALE AWAITS...</p>

  <div class="resort-scene" role="img" aria-label="Snow-covered lodge among trees in winter, stylised in greys"></div>

  <p class="airline-name">CORALWIND AIRWAYS</p>
  <svg class="social-mark" width="40" height="40" viewBox="0 0 40 40" aria-hidden="true">
    <rect x="0" y="0" width="40" height="40" fill="var(--social)"/>
  </svg>
  <p class="fine-print">Flights are from any Australian calital city flying Coralwind Airways<br>Accommodation is at The Nook Tervale (our own property)</p>
</main>
</body>
</html>
```